Web Design for ROLV Air conditioning company

Hello,

I am calling on you for the modernization of the company's website
https://clarovent-services-techniques.fr/

The new one must include the new logo with the new graphic charter (color, style ...)

I'm looking for a simple design (less is more), a font written without Serif, the logo that brings a touch of color and modernity.

(maintenance and installation company for air conditioning and ventilation systems)
COLORS: in line with the logo

CHAPTER:

# PRESENTATION
# SERVICES
AIR CONDITIONING (ice cube icon)
HEATING (flame icon)
AIR TREATMENT (icon fan)
# ACHIEVEMENTS

# CONTACT
CONTACT FORM
GOOGLE MAPS

Target Market(s)

Showcase site for our customers

Coding

Coded - Design and coding required

Number of Pages Required

4 page

Font styles to use
Sans Serif

Colors
33b8a4
33a6d7
3176b5
ffffff

Requirements
Must have
• Clear and fluid navigation
a visual identity of the page with the logo
Should not have
• Overloaded.

```html
<!DOCTYPE html>
<html lang="en">
<head>
<meta charset="utf-8">
<title>ROLV – Clarovent Services Techniques</title>
<link href="https://fonts.googleapis.com/css2?family=Montserrat:wght@500;700;800;900&family=Oswald:wght@400;500;600&family=Poppins:wght@400;500;600&display=swap" rel="stylesheet">
<style>
:root{
  --teal:#33b8a4;
  --sky:#33a6d7;
  --blue:#3176b5;
  --white:#ffffff;
  --dark:#2e3a46;
  --darker:#26313b;
  --ink:#1f2d3a;
  --grey:#c9d1d8;
}
*{box-sizing:border-box;margin:0;padding:0}
html,body{width:1200px;height:3492px;overflow:hidden}
body{position:relative;font-family:'Poppins',sans-serif;color:var(--white);
  background:linear-gradient(160deg,var(--teal) 0%,var(--sky) 50%,var(--blue) 100%)}
.abs{position:absolute}
.heading{font-family:'Oswald',sans-serif;text-transform:uppercase;font-weight:500}

/* header */
.site-header{left:0;top:0;width:1200px;height:72px;background:var(--white);display:flex;align-items:center;padding:0 24px}
.brand{display:flex;flex-direction:column;color:var(--teal)}
.brand-name{font-family:'Montserrat',sans-serif;font-weight:800;font-size:34px;line-height:1}
.brand-tag{font-size:10px;color:#7a8a96;letter-spacing:.5px}
.main-nav{position:absolute;left:480px;top:28px;display:flex;gap:30px;font-size:12px;font-weight:600;color:var(--ink)}
.call-btn{position:absolute;right:24px;top:20px;width:170px;height:32px;border-radius:16px;background:var(--teal);color:var(--white);font-size:12px;font-weight:600;display:flex;align-items:center;justify-content:center}

/* hero */
.callout{left:0;top:100px;width:1200px;text-align:center;font-family:'Oswald',sans-serif;font-size:22px;letter-spacing:.5px}
.callout svg{vertical-align:-4px;margin-right:10px}
.hero-title{left:180px;top:260px;font-family:'Montserrat',sans-serif;font-weight:800;font-size:48px;line-height:1.08;letter-spacing:1px}
.hero-tagline{left:632px;top:392px;font-family:'Montserrat',sans-serif;font-weight:800;font-size:24px;color:var(--ink)}
.hero-tagline span{color:var(--white);font-size:18px;margin-left:6px}

/* water treatment */
.water-title{left:100px;top:660px;width:440px;text-align:center;font-size:38px;line-height:1.15;color:var(--ink)}
.water-icon{left:280px;top:810px}
.check-list{left:630px;top:605px;list-style:none}
.check-list li{display:flex;align-items:center;gap:18px;height:44px;font-family:'Oswald',sans-serif;font-size:18px;text-transform:uppercase}

/* climate */
.climate{left:0;top:960px;width:1200px;height:330px;background:var(--dark)}
.steps{left:300px;top:20px;width:180px;text-align:center;list-style:none}
.steps li{display:flex;flex-direction:column;align-items:center;gap:14px;height:100px;font-family:'Oswald',sans-serif;text-transform:uppercase;font-size:18px;padding-top:8px}
.climate-title{left:640px;top:60px;width:340px;text-align:center;font-size:40px;line-height:1.15}
.climate-icon{left:760px;top:200px}

/* about */
.about-photo{left:0;top:1290px;width:1200px;height:810px;background:linear-gradient(120deg,#c9ced4 0%,#aab8c8 40%,#5b7fb8 75%,#c3c9d1 100%)}
.about-card{left:172px;top:1380px;width:490px;height:620px;background:var(--white);color:var(--ink);padding:0 30px}
.about-card h2{font-size:52px;color:var(--blue);text-align:center;margin-top:0;line-height:1.1}
.about-card h3{font-family:'Montserrat',sans-serif;font-weight:800;font-size:28px;line-height:1.1;margin-top:70px;text-transform:uppercase}
.feature{display:flex;align-items:center;gap:20px;margin-top:38px;font-family:'Oswald',sans-serif;font-size:18px;color:var(--blue);text-transform:uppercase}
.btn-dark{display:inline-flex;align-items:center;justify-content:center;width:290px;height:44px;border-radius:22px;background:var(--darker);color:var(--white);font-size:13px;font-weight:600;margin-top:60px;text-transform:uppercase}
.question{left:700px;top:1540px}

/* stats */
.stats{left:0;top:2160px;width:1200px;display:flex;justify-content:center;gap:150px}
.stat{display:flex;flex-direction:column;align-items:center;width:140px}
.stat-num{font-family:'Montserrat',sans-serif;font-weight:800;font-size:28px;margin-top:12px}
.stat-label{font-size:13px;font-weight:600;text-transform:uppercase}

/* services */
.services-band{left:0;top:2360px;width:1200px;height:120px;background:var(--dark);text-align:center}
.services-band h2{font-size:56px;line-height:1;padding-top:6px}
.band-icons{left:0;top:2432px;width:1200px;display:flex;justify-content:space-around;padding:0 220px}
.services-box{left:180px;top:2500px;width:840px;height:290px;background:#1f5a7a;display:flex;align-items:center;justify-content:space-around;text-align:center}
.services-box h3{font-size:52px;line-height:1.1;width:250px}
.service-links{left:180px;top:2808px;width:840px;display:flex;justify-content:space-around}
.btn-small{width:140px;height:30px;border-radius:15px;background:var(--darker);font-size:11px;font-weight:600;display:flex;align-items:center;justify-content:center;text-transform:uppercase}

/* footer */
.contact-info{left:220px;top:2930px;width:380px;font-size:13px;line-height:1.6}
.contact-info h4,.find-us h4,.follow h4{font-size:13px;font-weight:600;margin-bottom:12px}
.info-row{display:flex;gap:12px;align-items:flex-start;margin-bottom:16px}
.find-us{left:220px;top:3140px}
.map{width:380px;height:110px;background:linear-gradient(135deg,#dfe4e8,#bfc9d1);border-radius:2px}
.follow{left:220px;top:3300px}
.socials{display:flex;gap:16px}
.socials span{width:34px;height:34px;background:var(--white);display:block}
.form{left:672px;top:2928px;width:388px;height:412px;background:var(--darker);padding:18px 32px}
.form h4{font-family:'Oswald',sans-serif;font-size:24px;text-align:center;text-transform:uppercase;margin-bottom:14px;font-weight:500}
.field{background:var(--white);color:#8a96a0;font-size:12px;height:40px;padding:10px 14px;margin-bottom:12px}
.field.tall{height:92px}
.submit{width:70px;height:26px;background:var(--grey);color:var(--ink);font-size:11px;display:flex;align-items:center;justify-content:center}
.copyright{left:30px;top:3452px;font-size:13px;font-weight:600}
.to-top{right:20px;top:3420px}
</style>
</head>
<body>

<header class="site-header abs">
  <div class="brand"><span class="brand-name">ROLV</span><span class="brand-tag">Clarovent services techniques</span></div>
  <nav class="main-nav"><span>HOME</span><span>SERVICES ▾</span><span>ACHIEVEMENTS</span><span>CONTACT</span></nav>
  <div class="call-btn">CALL US</div>
</header>

<p class="callout abs"><svg width="26" height="26" viewBox="0 0 26 26"><rect width="26" height="26" rx="4" fill="#fff"/><path d="M8 6l3 0 1 4-2 1a9 9 0 0 0 5 5l1-2 4 1 0 3c-8 1-13-4-12-12z" fill="#33b8a4"/></svg>CALL US TODAY FOR A MAINTENANCE VISIT - 04 70 12 34 56</p>

<h1 class="hero-title abs">CLAROVENT<br>SERVICES<br>TECHNIQUES<br>GRENOBLE</h1>
<p class="hero-tagline abs">ROLV<span>"THE SPIRIT OF SERVICE"</span></p>

<h2 class="water-title heading abs">Maintenance of water treatment system</h2>
<svg class="water-icon abs" width="80" height="50" viewBox="0 0 80 50" aria-hidden="true"><g fill="none" stroke="#1f2d3a" stroke-width="6" stroke-linecap="round"><path d="M4 8q9-8 18 0t18 0 18 0 18 0"/><path d="M4 25q9-8 18 0t18 0 18 0 18 0"/><path d="M4 42q9-8 18 0t18 0 18 0 18 0"/></g></svg>

<ul class="check-list abs">
  <li><svg width="26" height="26" viewBox="0 0 26 26"><circle cx="13" cy="13" r="13" fill="#fff"/><path d="M7 13l4 4 8-8" stroke="#2e3a46" stroke-width="3" fill="none"/></svg>Soft water</li>
  <li><svg width="26" height="26" viewBox="0 0 26 26"><circle cx="13" cy="13" r="13" fill="#fff"/><path d="M7 13l4 4 8-8" stroke="#2e3a46" stroke-width="3" fill="none"/></svg>Osmotic water</li>
  <li><svg width="26" height="26" viewBox="0 0 26 26"><circle cx="13" cy="13" r="13" fill="#fff"/><path d="M7 13l4 4 8-8" stroke="#2e3a46" stroke-width="3" fill="none"/></svg>Maintenance of softeners</li>
  <li><svg width="26" height="26" viewBox="0 0 26 26"><circle cx="13" cy="13" r="13" fill="#fff"/><path d="M7 13l4 4 8-8" stroke="#2e3a46" stroke-width="3" fill="none"/></svg>Treatment of liquid effluents</li>
  <li><svg width="26" height="26" viewBox="0 0 26 26"><circle cx="13" cy="13" r="13" fill="#fff"/><path d="M7 13l4 4 8-8" stroke="#2e3a46" stroke-width="3" fill="none"/></svg>Calibration of pH probes</li>
  <li><svg width="26" height="26" viewBox="0 0 26 26"><circle cx="13" cy="13" r="13" fill="#fff"/><path d="M7 13l4 4 8-8" stroke="#2e3a46" stroke-width="3" fill="none"/></svg>Conductivity probe calibration</li>
  <li><svg width="26" height="26" viewBox="0 0 26 26"><circle cx="13" cy="13" r="13" fill="#fff"/><path d="M7 13l4 4 8-8" stroke="#2e3a46" stroke-width="3" fill="none"/></svg>Analog level management</li>
</ul>

<section class="climate abs">
  <ul class="steps abs">
    <li><svg width="30" height="30" viewBox="0 0 26 26"><circle cx="13" cy="13" r="13" fill="#33a6d7"/><path d="M7 13l4 4 8-8" stroke="#fff" stroke-width="3" fill="none"/></svg>Installation</li>
    <li><svg width="30" height="30" viewBox="0 0 26 26"><circle cx="13" cy="13" r="13" fill="#33a6d7"/><path d="M7 13l4 4 8-8" stroke="#fff" stroke-width="3" fill="none"/></svg>Maintenance</li>
    <li><svg width="30" height="30" viewBox="0 0 26 26"><circle cx="13" cy="13" r="13" fill="#33a6d7"/><path d="M7 13l4 4 8-8" stroke="#fff" stroke-width="3" fill="none"/></svg>Troubleshooting</li>
  </ul>
  <h2 class="climate-title heading abs">Reversible climate control</h2>
  <svg class="climate-icon abs" width="90" height="80" viewBox="0 0 90 80" aria-hidden="true"><g fill="none" stroke="#fff" stroke-width="4" stroke-linecap="round"><circle cx="30" cy="28" r="12"/><path d="M30 4v6M30 46v6M6 28h6M10 10l4 4M50 10l-4 4M10 46l4-4"/><path d="M34 52a12 12 0 0 1 4-22 16 16 0 0 1 30 4 10 10 0 0 1 2 18z" fill="#fff"/><path d="M44 62l-3 8M56 62l-3 8M68 62l-3 8"/></g></svg>
</section>

<div class="about-photo abs" role="img" aria-label="Photo of gloved hands handling white pipe fittings"></div>
<article class="about-card abs">
  <h2 class="heading">Who are we?</h2>
  <h3>We are<br>'Clarovent<br>Services<br>Techniques'</h3>
  <div class="feature"><svg width="60" height="30" viewBox="0 0 60 30"><rect y="4" width="60" height="6" fill="#3176b5"/><rect y="20" width="60" height="6" fill="#3176b5"/></svg>Laser lineage</div>
  <div class="feature"><svg width="60" height="40" viewBox="0 0 60 40"><circle cx="30" cy="20" r="19" fill="none" stroke="#3176b5" stroke-width="3"/><path d="M14 20q4-12 8 0t8 0 8 0 8 0" fill="none" stroke="#3176b5" stroke-width="3"/></svg>Vibration control</div>
  <div class="feature"><svg width="60" height="40" viewBox="0 0 60 40"><path d="M30 36L12 18a9 9 0 0 1 18-10 9 9 0 0 1 18 10z" fill="#3176b5"/></svg>Maintenance ventilation</div>
  <span class="btn-dark">Discover more</span>
</article>
<svg class="question abs" width="290" height="290" viewBox="0 0 290 290" aria-hidden="true"><circle cx="145" cy="145" r="145" fill="#fff"/><circle cx="145" cy="145" r="62" fill="none" stroke="#3176b5" stroke-width="12"/><text x="145" y="175" text-anchor="middle" font-family="Montserrat,sans-serif" font-weight="800" font-size="90" fill="#3176b5">?</text></svg>

<div class="stats abs">
  <div class="stat"><svg width="44" height="44" viewBox="0 0 44 44"><g fill="#fff"><circle cx="22" cy="10" r="6"/><circle cx="9" cy="16" r="4"/><circle cx="35" cy="16" r="4"/><path d="M12 38v-12a10 10 0 0 1 20 0v12z"/><path d="M2 38v-10a7 7 0 0 1 9-4v14zM42 38v-10a7 7 0 0 0-9-4v14z"/></g></svg><span class="stat-num">7 +</span><span class="stat-label">Clients</span></div>
  <div class="stat"><svg width="44" height="44" viewBox="0 0 44 44"><rect x="8" y="4" width="28" height="36" fill="none" stroke="#fff" stroke-width="3"/><path d="M14 14h16M14 22h16M14 30h10" stroke="#fff" stroke-width="3"/></svg><span class="stat-num">650 +</span><span class="stat-label">Contract</span></div>
  <div class="stat"><svg width="44" height="44" viewBox="0 0 44 44"><circle cx="22" cy="22" r="18" fill="none" stroke="#fff" stroke-width="3"/><circle cx="16" cy="18" r="2.5" fill="#fff"/><circle cx="28" cy="18" r="2.5" fill="#fff"/><path d="M14 27q8 8 16 0" fill="none" stroke="#fff" stroke-width="3"/></svg><span class="stat-num">590 +</span><span class="stat-label">Satisfied</span></div>
  <div class="stat"><svg width="44" height="44" viewBox="0 0 44 44"><circle cx="22" cy="22" r="20" fill="#fff"/><rect x="16" y="12" width="12" height="20" fill="none" stroke="#33a6d7" stroke-width="3"/></svg><span class="stat-num">1,752 +</span><span class="stat-label">Stock products</span></div>
</div>

<section class="services-band abs"><h2 class="heading">Services we provide</h2></section>
<div class="band-icons abs">
  <svg width="30" height="34" viewBox="0 0 30 34"><path d="M15 2c2 8 12 12 10 22a10 10 0 0 1-20 0c0-6 4-8 5-12 2 4 4 4 5 2z" fill="#33a6d7"/></svg>
  <svg width="34" height="34" viewBox="0 0 34 34"><path d="M17 2l14 8v14l-14 8-14-8V10z" fill="#33a6d7"/><path d="M3 10l14 8 14-8M17 18v14" stroke="#2e3a46" stroke-width="2" fill="none"/></svg>
  <svg width="34" height="34" viewBox="0 0 34 34"><g fill="#33a6d7"><circle cx="17" cy="17" r="4"/><path d="M17 13c-2-6 0-10 4-10 2 4-2 8-4 10zM21 17c6-2 10 0 10 4-4 2-8-2-10-4zM17 21c2 6 0 10-4 10-2-4 2-8 4-10zM13 17c-6 2-10 0-10-4 4-2 8 2 10 4z"/></g></svg>
</div>
<div class="services-box abs">
  <h3 class="heading">Heater</h3>
  <h3 class="heading">Air conditioner</h3>
  <h3 class="heading">Ventilation</h3>
</div>
<div class="service-links abs"><span class="btn-small">Know more</span><span class="btn-small">Know more</span><span class="btn-small">Know more</span></div>

<footer>
  <div class="contact-info abs">
    <h4>Reach Us</h4>
    <div class="info-row"><svg width="14" height="18" viewBox="0 0 14 18"><path d="M7 0a7 7 0 0 1 7 7c0 5-7 11-7 11S0 12 0 7a7 7 0 0 1 7-7z" fill="#fff"/><circle cx="7" cy="7" r="2.5" fill="#33a6d7"/></svg><span>12 Rue des Alpes,<br>38000 Grenoble</span></div>
    <div class="info-row"><svg width="14" height="14" viewBox="0 0 14 14"><path d="M2 1h3l1 3-2 1a7 7 0 0 0 4 4l1-2 3 1v3C6 12 1 7 2 1z" fill="#fff"/></svg><span>Tel: 04 70 12 34 56<br>Fax: 04 70 12 34 57</span></div>
    <div class="info-row"><svg width="16" height="12" viewBox="0 0 16 12"><rect width="16" height="12" fill="#fff"/><path d="M0 0l8 6 8-6" stroke="#33a6d7" fill="none"/></svg><span>contact@clarovent.fr</span></div>
  </div>
  <div class="find-us abs">
    <h4>Find Us</h4>
    <div class="map" role="img" aria-label="Map showing the Grenoble office location"></div>
  </div>
  <div class="follow abs">
    <h4>Follow Us</h4>
    <div class="socials"><span></span><span></span><span></span><span></span></div>
  </div>
  <form class="form abs">
    <h4>Send us a message</h4>
    <div class="field">Your Name</div>
    <div class="field">Your Email</div>
    <div class="field">Contact No.</div>
    <div class="field">Purpose Of Contact</div>
    <div class="field tall">Your Message</div>
    <div class="submit">Submit</div>
  </form>
  <p class="copyright abs">©2020, ROLV. All Rights Reserved.</p>
  <svg class="to-top abs" width="36" height="40" viewBox="0 0 36 40" aria-hidden="true"><path d="M18 2L2 20h10v18h12V20h10z" fill="#dfe6ea"/></svg>
</footer>

</body>
</html>
```